ultra-minimalist business card

front (black background, matte):

samir t. kouri
writer | photographer
get@samirkouri.com

back (white background, matte):

a picture speaks a thousand words;
a word draws a thousand pictures.

www.samirkouri.com

all text should be small (white or silver - as long as it shows against the black - on the front; black or gray - as long as it shows against the white - on the back).

feel free to get creative in terms of arrangement, alignment, and font type, but remember, the overall style is minimalist, so nothing too fancy, please.

thanks.

```html
<!DOCTYPE html>
<html lang="en">
<head>
<meta charset="utf-8">
<title>samir t. kouri — business card</title>
<link href="https://fonts.googleapis.com/css2?family=Cormorant+Garamond:ital,wght@1,400;1,500&display=swap" rel="stylesheet">
<style>
  :root {
    --backdrop: #d7ced3;
    --card-front: #0b0b0b;
    --card-back: #fafafa;
    --ink-light: #f2f2f2;
    --ink-silver: #a9a9a9;
    --ink-dark: #111111;
    --ink-grey: #6e6e6e;
    --nib-grey: #9a9a9a;
  }
  * { margin: 0; padding: 0; box-sizing: border-box; }
  html, body {
    width: 1200px;
    height: 900px;
    overflow: hidden;
    background: var(--backdrop);
    font-family: "Cormorant Garamond", Georgia, serif;
    font-style: italic;
  }
  .canvas {
    position: relative;
    width: 1200px;
    height: 900px;
  }
  .card {
    position: absolute;
    width: 520px;
    height: 300px;
    box-shadow: 0 6px 14px rgba(0,0,0,0.18);
  }
  .card--back { left: 130px; top: 130px; background: var(--card-back); }
  .card--front { left: 550px; top: 470px; background: var(--card-front); }

  /* back */
  .quote {
    position: absolute;
    left: 62px;
    top: 96px;
    color: var(--ink-dark);
  }
  .quote__small {
    display: block;
    font-size: 13px;
    line-height: 18px;
    color: var(--ink-grey);
  }
  .quote__large {
    display: block;
    font-size: 25px;
    line-height: 28px;
    font-weight: 500;
  }
  .quote__indent-1 { padding-left: 14px; }
  .quote__indent-2 { padding-left: 34px; }
  .quote__indent-3 { padding-left: 50px; }
  .nib-placeholder {
    position: absolute;
    left: 332px;
    top: 88px;
    width: 30px;
    height: 54px;
    background: var(--nib-grey);
  }
  .web {
    position: absolute;
    right: 36px;
    top: 150px;
    color: var(--ink-grey);
    font-size: 13px;
    letter-spacing: 0.3px;
  }

  /* front */
  .mark {
    position: absolute;
    left: 150px;
    top: 55px;
    width: 190px;
    height: 190px;
    border-radius: 50%;
    background: var(--ink-light);
    display: flex;
    align-items: center;
    justify-content: center;
  }
  .mark__name {
    color: var(--ink-dark);
    font-size: 28px;
    font-weight: 500;
  }
  .contact {
    position: absolute;
    right: 34px;
    top: 132px;
    text-align: right;
    color: var(--ink-silver);
    font-size: 14px;
    line-height: 1.3;
    letter-spacing: 0.3px;
  }
</style>
</head>
<body>
<main class="canvas">
  <section class="card card--back" aria-label="card back">
    <p class="quote">
      <span class="quote__small">a picture speaks</span>
      <span class="quote__large quote__indent-1">a thousand words;</span>
      <span class="quote__small quote__indent-2">a word draws</span>
      <span class="quote__large quote__indent-3">a thousand pictures.</span>
    </p>
    <div class="nib-placeholder" role="img" aria-label="small grey fountain pen nib drawing"></div>
    <p class="web">www.samirkouri.com</p>
  </section>

  <section class="card card--front" aria-label="card front">
    <div class="mark">
      <span class="mark__name">samir t. kouri</span>
    </div>
    <p class="contact">
      writer | photographer<br>
      get@samirkouri.com
    </p>
  </section>
</main>
</body>
</html>
```